Flyer-Design für Immobilienmakler
Zielgruppe
Immobilienmakler. Zielgruppe: Hausverkäufer im mittleren und älteren Alter.
Aufgabenstellung
Textvorschlag:
Eine kostenlose Immobilienbewertung bekommen Sie von jedem Makler, wir reduzieren zusätzlich unsere Vermittlungsprovision.
Sparen Sie jetzt 2 %* Provision
Alles wird teurer. Wir reduzieren die Provision!
Wir helfen bei der Verwirklichung Ihres Wohntraums. Angebot gültig gegen Vorlage des Flyers.
*Bei uns 2 % weniger:
• Übliche Maklerprovision 5,95 %
• 3,95 % bedeutet Alleinprovision oder geteilte Provision 1,97 %
• Gilt ab ein Verkaufswert von 400.000,- Euro
• Gültig bis 30. Dezember 2022
• Nur gegen Vorlage des Flyers
und Alleinauftrag.

```html
<!DOCTYPE html>
<html lang="de">
<head>
<meta charset="utf-8">
<title>ALVERA GmbH – Provisionsaktion</title>
<link rel="stylesheet" href="https://fonts.googleapis.com/css2?family=Montserrat:wght@400;600;700&family=Roboto:wght@500&display=swap">
<style>
  :root {
    --navy: #0d2b40;
    --lime: #b3cc33;
    --leaf: #3d8b3a;
    --rule: #5f7f55;
    --white: #ffffff;
  }
  * { margin: 0; padding: 0; box-sizing: border-box; }
  html, body { width: 846px; height: 1200px; overflow: hidden; background: var(--white); }
  .flyer {
    position: relative;
    width: 846px;
    height: 1200px;
    overflow: hidden;
    font-family: "Montserrat", sans-serif;
    color: var(--navy);
    background: var(--white);
  }
  .graphics { position: absolute; inset: 0; }
  .brand {
    position: absolute;
    left: 92px;
    top: 72px;
    display: flex;
    align-items: center;
    gap: 12px;
  }
  .brand-mark {
    width: 24px; height: 24px;
    background: var(--leaf);
  }
  .brand-name {
    font-family: "Montserrat", sans-serif;
    font-weight: 600;
    font-size: 30px;
    line-height: 36px;
    color: var(--navy);
    letter-spacing: 0.3px;
  }
  .tagline {
    position: absolute;
    left: 71px;
    top: 118px;
    font-family: "Roboto", sans-serif;
    font-weight: 500;
    font-size: 21.5px;
    color: var(--leaf);
    letter-spacing: 0.6px;
  }
  .offer-badge {
    position: absolute;
    left: 592px;
    top: 662px;
    width: 180px;
    height: 180px;
    border-radius: 50%;
    background: var(--lime);
    display: flex;
    align-items: center;
    justify-content: center;
  }
  .offer-text {
    transform: rotate(5deg);
    color: var(--white);
    text-align: center;
    font-size: 19.5px;
    line-height: 1.2;
    font-weight: 400;
    letter-spacing: 0.4px;
    margin-top: -6px;
  }
  .offer-text strong { font-weight: 700; }
  .headline {
    position: absolute;
    left: 72px;
    top: 826px;
    font-weight: 700;
    font-size: 40px;
    line-height: 50px;
    letter-spacing: -0.2px;
  }
  .headline .lead { color: var(--navy); display: block; }
  .headline .accent { color: var(--lime); display: block; }
  .intro {
    position: absolute;
    left: 73px;
    top: 952px;
    font-size: 19.3px;
    line-height: 24.5px;
    font-weight: 400;
    letter-spacing: 0.2px;
    white-space: nowrap;
  }
  .footnote {
    position: absolute;
    left: 63px;
    top: 1090px;
    font-size: 15.8px;
    line-height: 20px;
    font-weight: 400;
    white-space: nowrap;
  }
  .footnote span { display: block; padding-left: 10px; }
  .footnote span:first-child { padding-left: 0; }
</style>
</head>
<body>
<main class="flyer">
  <svg class="graphics" width="846" height="1200" viewBox="0 0 846 1200">
    <defs>
      <linearGradient id="houseTones" x1="0" y1="0" x2="0" y2="1">
        <stop offset="0" stop-color="#8fa3d6"/>
        <stop offset="0.25" stop-color="#b9b4d4"/>
        <stop offset="0.45" stop-color="#3f4a72"/>
        <stop offset="0.7" stop-color="#a9a7bf"/>
        <stop offset="0.88" stop-color="#c9a45a"/>
        <stop offset="1" stop-color="#5e8a3c"/>
      </linearGradient>
    </defs>
    <polygon class="accent-band" points="442,135 502,178 0,871 0,711" fill="#b3cc33"/>
    <polygon class="house-photo" role="img" aria-label="Foto: Einfamilienhaus mit Garage und Vorgarten in der Abenddämmerung"
      points="638,0 846,0 846,277 518,675 123,675" fill="url(#houseTones)"/>
    <polygon class="photo-tint" points="846,86 846,277 518,675 397,675" fill="#9cc21f" opacity="0.62"/>
    <rect class="base-rule" x="100" y="674" width="452" height="6" fill="#5f7f55"/>
  </svg>

  <header class="brand">
    <span class="brand-mark"></span>
    <span class="brand-name">ALVERA GmbH</span>
  </header>
  <p class="tagline">Ihr Partner für Wohnwerte</p>

  <div class="offer-badge">
    <p class="offer-text">Sparen Sie<br>jetzt <strong>2 %*</strong><br><strong>Provision</strong>!</p>
  </div>

  <h1 class="headline">
    <span class="lead">Alles wird teurer.</span>
    <span class="accent">Wir reduzieren die Provision!</span>
  </h1>

  <p class="intro">Eine kostenlose Immobilienbewertung bekommen Sie von jedem<br>Makler, wir reduzieren zusätzlich unsere Vermittlungsprovision und<br>helfen bei der Verwirklichung Ihres Wohntraums.</p>

  <p class="footnote">
    <span>* Gilt ab ein Verkaufswert von 400.000 €. Gültig bis 30. Dezember 2022.</span>
    <span>Nur gegen Vorlage des Flyers und Alleinauftrag.</span>
  </p>
</main>
</body>
</html>
```